VELDA NUTRITION WEBSITE DESIGN

We need a full design for the website to present the company to customers and partners.
We are ' Velda nutrition" based in New York. We develop Multivitamins, minerals and nutritional supplements to support immunity, general health and longevity. Our products include: Pregnancy supplements, Bone supplements and Iron supplements.
The design should convey trust, natural, health and growth, also relating to the different products that we sell.

I can not download the edited design and the designer didnt submit the last revised version yet.

```html
<!DOCTYPE html>
<html lang="en">
<head>
<meta charset="utf-8">
<title>Velda Nutrition</title>
<link href="https://fonts.googleapis.com/css2?family=Catamaran:wght@500;600&family=Montserrat:wght@400;500&display=swap" rel="stylesheet">
<style>
:root{
  --green:#8cc63f;
  --green-soft:#a7d46a;
  --leaf:#5f9a2a;
  --ink:#2b2b2b;
  --grey:#666;
  --purple:#6b3f8f;
  --blue:#1b3f9e;
  --red:#d3121c;
  --footer:#2f2f2f;
  --navy:#1f2a3c;
}
*{margin:0;padding:0;box-sizing:border-box}
html,body{width:1200px;height:3346px;overflow:hidden;background:#fff}
body{position:relative;font-family:"Montserrat",sans-serif;color:var(--ink)}
.abs{position:absolute}
.heading{font-family:"Catamaran",sans-serif;font-weight:600}
.brand{display:flex;align-items:center;gap:12px;font-family:"Catamaran",sans-serif;font-weight:500;font-size:34px;color:var(--ink)}
.brand .dot{width:30px;height:30px;border-radius:50%;background:var(--green)}
.nav{top:92px;left:423px;font-size:18px}
.nav a{position:absolute;white-space:nowrap;color:var(--ink);text-decoration:none}
.btn{display:flex;align-items:center;justify-content:center;border-radius:30px;color:#fff;font-size:19px;text-decoration:none}
.btn-green{background:var(--green)}
.hero-photo{top:139px;left:0;width:1200px;height:676px;
  background:
    radial-gradient(ellipse 260px 330px at 780px 360px,rgba(222,200,180,.55),transparent 70%),
    radial-gradient(ellipse 300px 260px at 790px 560px,rgba(175,182,192,.85),transparent 75%),
    radial-gradient(ellipse 220px 140px at 560px 560px,rgba(200,140,140,.45),transparent 75%),
    linear-gradient(90deg,#2f2d2b 0%,#3f3b37 30%,#6e655c 50%,#9a9ba1 72%,#c9ccd1 100%);}
.hero-title{top:305px;left:166px;font-size:54px;line-height:60px;color:#fff;white-space:nowrap}
.hero-sub{top:385px;left:150px;width:400px;text-align:center;font-size:19px;line-height:22px;color:#fff}
.bottles{top:585px;left:137px;width:386px;height:267px;border-radius:18px;
  background:linear-gradient(90deg,#ececef 0%,#f8f8fa 30%,#b28fc9 45%,#f4eef7 60%,#f8f8fa 75%,#e6e6ea 100%);}
.dots{top:690px;left:520px;display:flex;gap:17px}
.dots span{width:9px;height:9px;border-radius:50%;background:rgba(255,255,255,.55)}
.leaves{border-radius:50%;background:radial-gradient(ellipse at center,rgba(95,154,42,.55),rgba(140,198,63,.2) 55%,transparent 72%)}
.section-title{width:1200px;left:0;text-align:center;font-size:50px;color:var(--ink)}
.section-desc{width:1200px;left:0;text-align:center;font-size:17px;line-height:19px;color:#555}
.card{top:1108px;width:283px;height:389px;border:1.5px solid;background:#fff}
.card .shot{position:absolute;top:42px;left:28px;width:227px;height:165px;border-radius:8px}
.card h3{position:absolute;top:240px;width:100%;text-align:center;font-family:"Montserrat",sans-serif;font-weight:500;font-size:20px}
.card p{position:absolute;top:275px;left:36px;width:211px;text-align:center;font-size:12px;line-height:15px;color:#333}
.card .btn{position:absolute;top:323px;left:65px;width:153px;height:42px}
.about-band{top:1687px;left:420px;width:780px;height:518px;background:var(--green);border-radius:0 300px 300px 0/0 260px 260px 0}
.about-photo{top:1580px;left:0;width:650px;height:625px;
  background:
    radial-gradient(ellipse 90px 120px at 390px 110px,rgba(226,196,140,.95),transparent 75%),
    radial-gradient(ellipse 200px 330px at 370px 400px,rgba(64,110,168,.95),transparent 75%),
    linear-gradient(90deg,#6a5a46 0%,#8a6c50 30%,#5a7aa6 55%,rgba(140,198,63,0) 100%);}
.about-title{top:1820px;left:672px;font-size:50px;color:#fff}
.about-text{top:1890px;left:672px;width:440px;font-size:16.5px;line-height:23.6px;color:#fff}
.develop{top:2480px;width:300px;text-align:center}
.develop .ring{width:116px;height:116px;margin:0 auto;border:3px solid var(--green);border-radius:50%;display:flex;align-items:center;justify-content:center}
.develop h4{margin-top:34px;font-family:"Montserrat",sans-serif;font-weight:500;font-size:22px;line-height:27px;color:#555}
.develop p{margin-top:20px;font-size:13px;line-height:21px;color:#777}
.footer{top:2890px;left:0;width:1200px;height:456px;background:var(--footer);color:#fff}
.footer h5{position:absolute;top:80px;font-family:"Montserrat",sans-serif;font-weight:400;font-size:22px;color:var(--green)}
.footer .links{position:absolute;top:138px;left:425px;font-size:13px;line-height:22.5px}
.contact-row{position:absolute;left:572px;display:flex;align-items:center;gap:14px;font-size:13px;line-height:22px}
.contact-row .ic{width:40px;height:40px;border-radius:50%;background:var(--green);display:flex;align-items:center;justify-content:center;flex:none}
.email{position:absolute;top:185px;left:830px;width:236px;height:42px;border-radius:21px;background:#fff;color:#333;font-size:14px;display:flex;align-items:center;padding-left:18px}
.email .go{position:absolute;right:3px;top:3px;width:36px;height:36px;border-radius:50%;background:#fff;border:2px solid var(--green);display:flex;align-items:center;justify-content:center}
.rule{position:absolute;top:356px;left:128px;width:938px;height:1px;background:#555}
.copy{position:absolute;top:390px;width:1200px;text-align:center;font-size:12px}
</style>
</head>
<body>

<header>
  <div class="abs brand" style="top:52px;left:102px"><span class="dot"></span>Velda Nutrition</div>
  <svg class="abs" style="top:33px;left:788px" width="22" height="22" viewBox="0 0 22 22" fill="none" stroke="#888" stroke-width="2"><circle cx="9" cy="9" r="7"/><path d="M14 14l6 6"/></svg>
  <svg class="abs" style="top:31px;left:834px" width="22" height="24" viewBox="0 0 22 24" fill="none" stroke="#888" stroke-width="2"><circle cx="11" cy="7" r="5"/><path d="M2 23c0-6 4-9 9-9s9 3 9 9z"/></svg>
  <svg class="abs" style="top:32px;left:876px" width="26" height="22" viewBox="0 0 26 22" fill="none" stroke="#888" stroke-width="2"><path d="M13 20S2 13 2 7a5.5 5.5 0 0 1 11-1 5.5 5.5 0 0 1 11 1c0 6-11 13-11 13z"/></svg>
  <a class="abs btn btn-green" style="top:26px;left:942px;width:153px;height:40px;font-size:18px">Order Now</a>
  <nav class="abs nav">
    <a style="left:0;color:var(--green)">Home</a>
    <a style="left:104px">About</a>
    <a style="left:209px">Products</a>
    <a style="left:338px">Why Choose us</a>
    <a style="left:523px">Blog</a>
    <a style="left:614px">Contact</a>
  </nav>
</header>

<section>
  <div class="abs hero-photo" role="img" aria-label="Pregnant woman sitting on a bed holding a glass of water and supplement pills"></div>
  <h1 class="abs heading hero-title">Velda Nutrition</h1>
  <p class="abs hero-sub">Lorem ipsum dolor sit amet, consectetur adipiscing elit, sed do eiusmod temp</p>
  <a class="abs btn btn-green" style="top:449px;left:272px;width:153px;height:40px">Order Now</a>
  <div class="abs dots"><span></span><span></span><span></span><span></span><span></span></div>
  <div class="abs bottles" role="img" aria-label="Three pregnancy supplement bottles"></div>
</section>

<section>
  <h2 class="abs heading section-title" style="top:945px">Our Products</h2>
  <p class="abs section-desc" style="top:1018px">Lorem ipsum dolor sit amet, consectetur adipiscing elit, sed do eiusmod<br>tempor incididunt ut labore et dolore magna aliquauis ipsum.</p>

  <div class="abs card" style="left:132px;border-color:#b9a3cc">
    <div class="shot" role="img" aria-label="Pregnancy supplement bottles" style="background:linear-gradient(90deg,#ececef 0%,#f7f7f9 30%,#9a6fb8 47%,#efe4f4 62%,#f7f7f9 75%,#e6e6ea 100%)"></div>
    <h3 style="color:var(--purple)">Pregnancy supplements</h3>
    <p>Lorem ipsum dolor sit amet, conse ctetur adipiscing elit, sed dlo.</p>
    <a class="btn" style="background:var(--purple)">Order Now</a>
  </div>
  <div class="abs card" style="left:458px;border-color:#7d95cf">
    <div class="shot" role="img" aria-label="Bone supplement bottles" style="background:linear-gradient(90deg,#ececef 0%,#f7f7f9 30%,#3d5fb8 47%,#e4eaf6 62%,#f7f7f9 75%,#e6e6ea 100%)"></div>
    <h3 style="color:var(--blue)">Bone supplements</h3>
    <p>Lorem ipsum dolor sit amet, conse ctetur adipiscing elit, sed dlo.</p>
    <a class="btn" style="background:var(--blue)">Order Now</a>
  </div>
  <div class="abs card" style="left:783px;border-color:#e58b8f">
    <div class="shot" role="img" aria-label="Iron supplement bottles" style="background:linear-gradient(90deg,#ececef 0%,#f7f7f9 30%,#c8262e 47%,#f6e2e2 62%,#f7f7f9 75%,#e6e6ea 100%)"></div>
    <h3 style="color:var(--red)">Iron supplements</h3>
    <p>Lorem ipsum dolor sit amet, conse ctetur adipiscing elit, sed dlo.</p>
    <a class="btn" style="background:var(--red)">Order Now</a>
  </div>
</section>

<div class="abs leaves" style="top:1530px;left:0;width:230px;height:140px" role="img" aria-label="Scattered green leaves"></div>

<section>
  <div class="abs about-band"></div>
  <div class="abs about-photo" role="img" aria-label="Pregnant woman in a denim shirt reading a supplement bottle in a store"></div>
  <h2 class="abs heading about-title">About VELDA</h2>
  <p class="abs about-text">Lorem ipsum dolor sit amet, consectetur adipiscing elit, sed do eiusmod tempor incididunt ut labore et dolore magna aliquauis ipsum. Lorem ipsum dolor sit amet, consectetur adipiscing elit, sed do eiusmod tempor incididunt ut labore et dolore magna aliquauis ipsum. Lorem ipsum dolor sit amet, consectetur adipiscing elit, sed do eiusmod tempor incididunt ut labore et dolore magna aliquauis ipsum.</p>
</section>

<div class="abs leaves" style="top:2270px;left:0;width:230px;height:140px" role="img" aria-label="Scattered green leaves"></div>
<div class="abs leaves" style="top:2750px;left:850px;width:290px;height:140px" role="img" aria-label="Scattered green leaves"></div>

<section>
  <h2 class="abs heading section-title" style="top:2287px">What We Develop</h2>
  <p class="abs section-desc" style="top:2360px">Lorem ipsum dolor sit amet, consectetur adipiscing elit, sed do eiusmod<br>tempor incididunt ut labore et dolore magna aliquauis ipsum.</p>

  <div class="abs develop" style="left:130px">
    <div class="ring"><svg width="56" height="56" viewBox="0 0 56 56" fill="var(--navy)"><path d="M28 28V14M28 18c-8 0-12-5-12-10 7 0 12 4 12 10zM28 18c8 0 12-5 12-10-7 0-12 4-12 10z" stroke="var(--navy)" stroke-width="3" fill="none"/><rect x="8" y="32" width="22" height="12" rx="6" fill="none" stroke="var(--navy)" stroke-width="3"/><rect x="26" y="36" width="22" height="12" rx="6"/></svg></div>
    <h4>Multivitamins</h4>
    <p>Lorem ipsum dolor sit amet, consectetur adipiscing elit, sed do eiusmod tempor incididunt ut labore et sed do eiusmod tempor incididunt ut labore etd</p>
  </div>
  <div class="abs develop" style="left:450px">
    <div class="ring"><svg width="56" height="56" viewBox="0 0 56 56" fill="var(--navy)"><rect x="20" y="6" width="20" height="8" rx="2"/><rect x="16" y="14" width="28" height="36" rx="5"/><circle cx="30" cy="32" r="7" fill="#fff"/><rect x="6" y="28" width="12" height="22" rx="3"/></svg></div>
    <h4>Minerals &amp; nutritional supplements</h4>
    <p>Lorem ipsum dolor sit amet, consectetur adipiscing elit, sed do eiusmod tempor incididunt ut labore et dolore ma</p>
  </div>
  <div class="abs develop" style="left:777px">
    <div class="ring"><svg width="56" height="56" viewBox="0 0 56 56" fill="var(--navy)"><rect x="8" y="10" width="16" height="6" rx="2"/><rect x="6" y="16" width="20" height="32" rx="4"/><rect x="30" y="18" width="18" height="6" rx="2"/><rect x="28" y="24" width="22" height="24" rx="4"/><path d="M34 42c0-8 6-12 11-12 0 7-5 12-11 12z" fill="#fff"/></svg></div>
    <h4>Health and<br>Longevity</h4>
    <p>Lorem ipsum dolor sit amet, consectetur adipiscing elit, sed do eiusmod tempor incididunt ut labore et dolore ma</p>
  </div>
</section>

<footer class="abs footer">
  <div class="abs brand" style="top:88px;left:152px;color:#fff"><span class="dot"></span>Velda Nutrition</div>
  <p class="abs" style="top:178px;left:150px;width:240px;font-size:13px;line-height:19px">Lorem ipsum dolor sit amelor conse ctet ur adipisclorem ipsumilit, sed do eiusmod tempor incididunt ut labore et dolore magna aliqua. Quis ipsum suspendisse ultrices gravida</p>

  <h5 style="left:425px">Links</h5>
  <div class="links">Home<br>About<br>Products<br>My Account<br>FAQ's<br>Why Choose us<br>Contact</div>

  <h5 style="left:581px">Contact Us</h5>
  <div class="contact-row" style="top:138px">
    <span class="ic"><svg width="16" height="20" viewBox="0 0 16 20" fill="#fff"><path d="M8 0a8 8 0 0 0-8 8c0 6 8 12 8 12s8-6 8-12a8 8 0 0 0-8-8z"/><circle cx="8" cy="8" r="3" fill="var(--green)"/></svg></span>
    <span style="margin-top:6px">Location Name<br>Dummy addess livv<br>Oregon 6425 PE (2004)</span>
  </div>
  <div class="contact-row" style="top:219px">
    <span class="ic"><svg width="18" height="18" viewBox="0 0 24 24" fill="#fff"><path d="M6.6 10.8a15 15 0 0 0 6.6 6.6l2.2-2.2a1 1 0 0 1 1-.25 11.4 11.4 0 0 0 3.6.6 1 1 0 0 1 1 1V20a1 1 0 0 1-1 1A17 17 0 0 1 3 4a1 1 0 0 1 1-1h3.5a1 1 0 0 1 1 1 11.4 11.4 0 0 0 .6 3.6 1 1 0 0 1-.25 1z"/></svg></span>
    <span>Phone:555.014.0198</span>
  </div>
  <div class="contact-row" style="top:272px">
    <span class="ic"><svg width="18" height="14" viewBox="0 0 18 14" fill="#fff"><path d="M0 0h18v14H0z"/><path d="M1 1l8 6 8-6" stroke="var(--green)" stroke-width="1.5" fill="none"/></svg></span>
    <span>Email info@veldanutrition.example</span>
  </div>

  <h5 style="left:831px">Newsletter Sign up</h5>
  <p class="abs" style="top:135px;left:830px;width:240px;font-size:12.5px;line-height:16px">Lorem ipsum dolor sit amelor conse ctet ur adipisclorem ipsumilit,</p>
  <div class="email">Email<span class="go"><svg width="20" height="14" viewBox="0 0 20 14" fill="none" stroke="var(--green)" stroke-width="2"><path d="M0 7h18M12 1l6 6-6 6"/></svg></span></div>

  <div class="rule"></div>
  <p class="copy">© 2022 All Rights Reserved.Terms &amp; Conditions Privacy Policy</p>
</footer>

</body>
</html>
```